Corporate A3 Deskpad Design For Services Company

We need a design for a A3 desk pad for our clients with our information around the sides. Please find attached our logo, examples and other collateral that we have for inspiration.
Please see below for the details on what we want.
The colours are in both the A4 brochure design and the logo as well as our website www.brimwelltech.com.au.
Thanks,
RM
Target Market(s)
Corporate
Industry/Entity Type
It Company
Font styles to use
Sans Serif
Colors
Designer to choose colors to be used in the design.
Requirements
Must have
- We simply want a simple corporate design in our colours around the sides. The top left will have our contact information (name, phone, email, website etc). Underneath that will be filler text with 1 heading and text underneath. on the right will have 3 sections each with a heading.
Should not have
- Calendars

```html
<!DOCTYPE html>
<html lang="en">
<head>
<meta charset="utf-8">
<title>Brimwell Desk Pad</title>
<link href="https://fonts.googleapis.com/css2?family=Roboto:wght@400;500;700&display=swap" rel="stylesheet">
<style>
  :root {
    --backdrop: #ece9e4;
    --orange: #f5a833;
    --orange-pale: #fbd9a0;
    --paper: #ffffff;
    --ink: #555560;
    --rule: #a8a8ae;
    --band: #4a4a52;
    --photo-tone-a: #d9d9dc;
    --photo-tone-b: #a9a7aa;
  }
  * { box-sizing: border-box; margin: 0; padding: 0; }
  html, body {
    width: 1200px; height: 932px; overflow: hidden;
    background: var(--backdrop);
    font-family: "Roboto", Arial, sans-serif;
  }
  .deskpad {
    position: absolute; left: 40px; top: 103px;
    width: 1120px; height: 726px;
    background: linear-gradient(to bottom, var(--orange-pale) 0, var(--orange-pale) 26%, var(--orange) 27%, var(--orange) 100%);
  }
  .sheet {
    position: absolute; left: 16px; right: 16px; top: 0; bottom: 16px;
    background: var(--paper);
  }
  .brand-name {
    position: absolute; left: 23px; top: 22px;
    font-size: 26px; font-weight: 500; line-height: 30px;
    color: var(--ink);
  }
  .contact {
    position: absolute; left: 23px; top: 64px;
    font-size: 10px; line-height: 13px; color: var(--ink);
  }
  .contact .gap { height: 10px; }
  .contact b { color: var(--orange); font-weight: 500; }
  .label {
    position: absolute;
    font-size: 12px; font-weight: 700; color: var(--ink);
    letter-spacing: 0.3px;
  }
  .rules {
    position: absolute;
    background: repeating-linear-gradient(to bottom,
      var(--rule) 0, var(--rule) 1.5px, transparent 1.5px, transparent 9.5px);
  }
  .notes-label { left: 23px; top: 160px; }
  .notes-rules { left: 23px; top: 192px; width: 167px; height: 330px; }
  .col-right { left: 904px; width: 167px; }
  .h1 { top: 25px; }
  .h1-rules { top: 53px; height: 105px; }
  .h2 { top: 197px; }
  .h2-rules { top: 225px; height: 115px; }
  .h3 { top: 376px; }
  .h3-rules { top: 402px; height: 105px; }
  .footer-band {
    position: absolute; left: 10px; right: 0; top: 576px; height: 125px;
    background: var(--band);
    text-align: center;
  }
  .photo {
    position: absolute; top: 10px; width: 100px; height: 100px;
    border: 2px solid #ffffff;
    background: linear-gradient(135deg, var(--photo-tone-a), var(--photo-tone-b));
  }
  .photo-left { left: 16px; }
  .photo-right { right: 16px; }
  .services {
    margin-top: 10px;
    font-size: 12px; font-weight: 700; color: var(--orange);
    letter-spacing: 0.2px; word-spacing: 1px;
  }
  .tagline {
    margin-top: 17px;
    font-size: 21px; font-weight: 500; color: #ffffff;
  }
  .web {
    margin-top: 2px;
    font-size: 12px; font-weight: 700; color: var(--orange);
  }
  .social {
    margin-top: 13px;
    display: flex; justify-content: center; gap: 12px;
  }
  .social span {
    width: 22px; height: 22px; border-radius: 50%; background: #ffffff;
  }
</style>
</head>
<body>
  <div class="deskpad">
    <div class="sheet">
      <div class="brand-name">Brimwell</div>
      <div class="contact">
        48 Harlow St<br>
        Northgate QLD 4013
        <div class="gap"></div>
        <b>t:</b> 1300 555 014<br>
        <b>e:</b> info@brimwelltech.com.au
      </div>

      <div class="label notes-label">NOTES</div>
      <div class="rules notes-rules"></div>

      <div class="label col-right h1">HEADING 1</div>
      <div class="rules col-right h1-rules"></div>
      <div class="label col-right h2">HEADING 2</div>
      <div class="rules col-right h2-rules"></div>
      <div class="label col-right h3">HEADING 3</div>
      <div class="rules col-right h3-rules"></div>

      <div class="footer-band">
        <div class="photo photo-left" role="img" aria-label="Photo of a hand pressing a ceiling smoke alarm"></div>
        <div class="photo photo-right" role="img" aria-label="Photo of a technician servicing a smoke alarm"></div>
        <div class="services">SMOKE ALARM COMPLIANCE &nbsp;&nbsp;| &nbsp;AIR CONDITION CLEANING &nbsp;| &nbsp;SAFETY SWITCH TESTING</div>
        <div class="tagline">Safety First. Don’t Take the Risk.</div>
        <div class="web">www.brimwelltech.com.au</div>
        <div class="social" aria-label="Social media links">
          <span></span><span></span><span></span>
        </div>
      </div>
    </div>
  </div>
</body>
</html>
```